Elegant brochure design for startup

We want to design an advertising booklet to introduce our company as a professional and trustworthy.

please take a look at the attached content templet to read know more about our business and services. Also to see what each page of the booklet should contain.

The size of the booklet should be around the half of A4 page. 12 pages includes the cover and back page ( See content templet attached )

We will provide content, pictures, and logo and our specifications for the
designer

Target Market(s)

We want to target executives in private and government sectors, the decision makers who are open to new and fresh ideas

Industry/Entity Type

Business Consultant

Font styles to use
Sans Serif

Requirements
Must have
• - Attractive, elegant, eyes catching design inspired attached identity.
• - bright color background for the writhing to make it easier for readers
• - neat arrangement of the content throughout the booklet. For example, arranging the content in a boxes using colors etc. to make easier for the reader.
Nice to have
• - icons to explane some of the content.
• - Info-graphic style when it make the content (in some parts easer to read )
• - Simple and elegant
• - We have a simi human icon as the letter "i" in our logo .. you may use it in some forms to represent human icon. Also you can modify it to represent deferent human format (Doctors - women - factory employee etc.
Should not have
• - don't use human pictures ! we prefer to use graphic abstract shapes and colors.
• - We don't prefer crowded pages ..
• - Our work is all about LOCAL organizational culture and employees. We are taking about the local market and as you know our local uniform is deferent than the western dress uniform. That's way we don't want to put a pic with a man in suit or women in short uniform. You can use icon like the ones when you search ( saudi employee icon) (without showing the faces - shadow format)

```html
<!DOCTYPE html>
<html lang="en">
<head>
<meta charset="utf-8">
<title>Brightfold Culture – Booklet Spread</title>
<link href="https://fonts.googleapis.com/css2?family=Quicksand:wght@500;600;700&display=swap" rel="stylesheet">
<style>
  :root {
    --backdrop: #e9ecef;
    --paper: #ffffff;
    --teal: #1fb7cf;
    --teal-light: #8fd4e6;
    --teal-pale: #c4e8f2;
    --teal-mid: #2a9fc4;
    --navy: #1b5a97;
    --ink: #1d4f83;
  }
  * { margin: 0; padding: 0; box-sizing: border-box; }
  html, body {
    width: 1200px; height: 900px; overflow: hidden;
    background: var(--backdrop);
    font-family: "Quicksand", sans-serif;
    color: var(--ink);
  }
  .spread {
    position: absolute; left: 40px; top: 54px;
    width: 1120px; height: 792px;
    display: flex;
    box-shadow: 0 10px 30px rgba(0,0,0,.12);
  }
  .page {
    position: relative; width: 560px; height: 792px;
    background: var(--paper); overflow: hidden;
  }
  .page--left { border-right: 1px solid #e3e7ea; }
  .page-art { position: absolute; inset: 0; }
  .brand {
    position: absolute; color: #fff; font-weight: 700;
    line-height: 1; text-transform: lowercase;
  }
  .brand__name { font-size: 22px; display: block; }
  .brand__sub { font-size: 17px; display: block; font-weight: 700; letter-spacing: 1px; }
  .page--left .brand { right: 34px; top: 22px; text-align: right; }
  .page--right .brand { left: 44px; top: 48px; }
  .page-number {
    position: absolute; bottom: 22px; color: #fff;
    font-size: 15px; font-weight: 600; letter-spacing: 1px;
  }
  .page--left .page-number { left: 36px; }
  .page--right .page-number { right: 36px; }

  .pillar { position: absolute; left: 248px; width: 260px; }
  .pillar__title {
    font-size: 30px; font-weight: 600; letter-spacing: 1px;
    color: var(--navy); padding-bottom: 6px;
    border-bottom: 3px solid var(--teal); display: inline-block;
    padding-right: 30px; margin-bottom: 8px;
  }
  .pillar__text { font-size: 14px; font-weight: 600; line-height: 1.3; }
  .pillar--attract { top: 160px; }
  .pillar--engage { top: 340px; }
  .pillar--retain { top: 505px; }

  .pillar-icon { position: absolute; left: 58px; }
  .pillar-icon--attract { top: 118px; }
  .pillar-icon--engage { top: 296px; }
  .pillar-icon--retain { top: 468px; }

  .intro {
    position: absolute; left: 172px; top: 150px; width: 340px;
    font-size: 14.5px; font-weight: 600; line-height: 1.32;
    text-align: justify;
  }
  .intro p + p { margin-top: 18px; }
  .intro--tail {
    position: absolute; left: 300px; top: 438px; width: 212px;
    font-size: 14.5px; font-weight: 600; line-height: 1.32; text-align: justify;
  }
  .service-cluster { position: absolute; left: 34px; top: 400px; }
</style>
</head>
<body>
<main class="spread">

  <section class="page page--left">
    <svg class="page-art" width="560" height="792" viewBox="0 0 560 792" aria-hidden="true">
      <polygon points="290,0 560,0 560,150" fill="var(--teal-pale)"/>
      <polygon points="350,0 560,0 560,96 420,96" fill="var(--teal)"/>
      <polygon points="0,600 560,700 560,792 0,792" fill="var(--teal-light)"/>
      <polygon points="0,650 230,700 560,740 560,792 0,792" fill="var(--teal)"/>
    </svg>
    <div class="brand"><span class="brand__name">brightfold</span><span class="brand__sub">culture</span></div>

    <svg class="pillar-icon pillar-icon--attract" width="150" height="150" viewBox="0 0 150 150" role="img" aria-label="Attract icon: group of stylised people in a dark blue hexagon">
      <polygon points="75,0 150,37 150,113 75,150 0,113 0,37" fill="var(--navy)"/>
    </svg>
    <svg class="pillar-icon pillar-icon--engage" width="150" height="150" viewBox="0 0 150 150" role="img" aria-label="Engage icon: people with rising chart in a teal hexagon">
      <polygon points="75,0 150,37 150,113 75,150 0,113 0,37" fill="var(--teal)"/>
    </svg>
    <svg class="pillar-icon pillar-icon--retain" width="130" height="130" viewBox="0 0 130 130" role="img" aria-label="Retain illustration: connected team of people in light blue">
      <defs>
        <linearGradient id="retain-fill" x1="0" y1="0" x2="1" y2="1">
          <stop offset="0" stop-color="var(--teal-pale)"/>
          <stop offset="1" stop-color="var(--teal-light)"/>
        </linearGradient>
      </defs>
      <polygon points="65,0 130,32 130,98 65,130 0,98 0,32" fill="url(#retain-fill)"/>
    </svg>

    <article class="pillar pillar--attract">
      <h2 class="pillar__title">ATTRACT</h2>
      <p class="pillar__text">the top talent available in the workforce market by optimizing their workplace to become a workplace of choice.</p>
    </article>
    <article class="pillar pillar--engage">
      <h2 class="pillar__title">ENGAGE</h2>
      <p class="pillar__text">human capital to the best of their abilities and increase performance and productivity; and</p>
    </article>
    <article class="pillar pillar--retain">
      <h2 class="pillar__title">RETAIN</h2>
      <p class="pillar__text">the top talent by connecting them mentally and emotionally to their workplace.</p>
    </article>
    <span class="page-number">01</span>
  </section>

  <section class="page page--right">
    <svg class="page-art" width="560" height="792" viewBox="0 0 560 792" aria-hidden="true">
      <polygon points="360,0 560,0 560,120" fill="var(--teal-pale)"/>
      <polygon points="440,40 560,40 560,110" fill="var(--teal-light)"/>
      <polygon points="0,30 400,30 460,110 0,110" fill="var(--teal)"/>
      <polygon points="0,680 560,640 560,792 0,792" fill="var(--teal-light)"/>
      <polygon points="0,740 300,710 560,700 560,792 0,792" fill="var(--teal)"/>
    </svg>
    <div class="brand"><span class="brand__name">brightfold</span><span class="brand__sub">culture</span></div>

    <div class="intro">
      <p>BRIGHTFOLD CULTURE is a team of employee engagement, internal communication, and organizational culture experts with both local and international backgrounds. With our expertise and longstanding experience, we can help organizations like yours to diagnose problems optimally, to measure your employee engagement level, and to handle workplace related challenges in organizational culture and internal communications.</p>
      <p>We know the right practices and the path that leads to business success and high employee engagement rates. We are willing to work side by side with you to help you achieve your goals,</p>
    </div>
    <div class="intro--tail">attract and engage the right candidates, align them with your organization's values and objectives, and create the best organizational culture to guarantee high retention rates.</div>

    <svg class="service-cluster" width="280" height="300" viewBox="0 0 280 300" role="img" aria-label="Service icons in hexagons: health and business tools, people, growth chart and globe">
      <polygon points="70,0 130,30 130,100 70,130 10,100 10,30" fill="var(--teal)"/>
      <polygon points="170,60 230,90 230,160 170,190 110,160 110,90" fill="var(--teal-mid)"/>
      <polygon points="70,110 130,140 130,210 70,240 10,210 10,140" fill="var(--teal-light)"/>
      <polygon points="140,180 200,210 200,270 140,300 80,270 80,210" fill="var(--teal-pale)"/>
    </svg>
    <span class="page-number">02</span>
  </section>

</main>
</body>
</html>
```